vale corvan website design

An IT support and IT Security Company - just use dummy text for now for the design. Examples of sites we like the looks and feel of but need it more professional feel are like: www.brontahelpdesk.uk.com , www.quillmoor.co.uk, www.harvestine.com/professional/, www.dulo.com, www.fenwix.com,

Best to message me if you have any questions

Target Market(s)

small to medium UK based companies that require IT support services

Industry/Entity Type

It Company

Contact Information for Business Card

use dummy name, telephone and email for now, will provide details later.

Logo Text

vale corvan (and then below the logo it should say "your IT, networks and security partner")

Coding

Coded - Design and coding required

Number of Pages Required

5+ page

Colors

Designer to choose colors to be used in the design.

Requirements
Must have
• must be professional, yet simple and clear that this is a serious IT support and IT security company.
Nice to have
• 1)The website homepage must have professional quality pictures of IT support or London city skyline or any picture that projects friendly business partners, professionalism and ready to serve.
• 2) Home page needs to include tabs for following pages 'Services' , 'About Us' , 'Contact Us' 'Home'
• 3) Website built customised using wordpress is ideal and easy for us to manage.
• more room for boxed options from homepage (with pic or image in background)
Should not have
• no checkout trolleys or payment options.

```html
<!DOCTYPE html>
<html lang="en">
<head>
<meta charset="utf-8">
<title>vale corvan — IT support and IT security</title>
<link href="https://fonts.googleapis.com/css2?family=Poppins:wght@400;500;600&family=Open+Sans:wght@400;600&display=swap" rel="stylesheet">
<style>
:root{
  --ink:#1f2a36;
  --text:#5b6470;
  --muted:#8a929b;
  --dark:#28323e;
  --dark-2:#222b35;
  --green:#2bb24c;
  --orange:#f2602f;
  --blue:#1a95de;
  --blue-deep:#0f86d2;
  --line:#e6e9ec;
  --soft:#f6f7f9;
  --white:#ffffff;
}
*{box-sizing:border-box;margin:0;padding:0}
html,body{width:1200px;height:3704px;overflow:hidden}
body{position:relative;background:var(--white);font-family:"Open Sans",Arial,sans-serif;color:var(--text)}
.abs{position:absolute}
h1,h2,h3,h4,.head{font-family:"Poppins",Arial,sans-serif;color:var(--ink);font-weight:500}

/* top bar */
.topbar{left:0;top:0;width:1200px;height:80px;background:var(--white)}
.brand{font-family:"Poppins",Arial,sans-serif;font-weight:600;font-size:24px;color:var(--ink);letter-spacing:.2px;line-height:1.1}
.logo{display:flex;flex-direction:column}
.tagline{font-family:"Open Sans",Arial,sans-serif;font-size:10.5px;color:var(--text);margin-top:3px;letter-spacing:.2px;white-space:nowrap}
.topbar .logo{left:88px;top:17px}
.contact-item{display:flex;align-items:center;gap:10px;font-size:14px;color:var(--ink);line-height:1.25}
.contact-item small{display:block;font-size:12px;color:var(--text)}
.lang{left:1068px;top:30px;font-size:12px;color:var(--ink);display:flex;gap:6px;align-items:center}

/* nav */
.nav{left:0;top:80px;width:1200px;height:52px;background:var(--dark);display:flex;justify-content:center;gap:40px;align-items:center;padding-right:10px}
.nav a{font-family:"Poppins",Arial,sans-serif;color:var(--white);font-size:14px;text-decoration:none;position:relative;font-weight:500}
.nav a.active{color:#c9d1d9;font-weight:400}
.nav a.active::before{content:"";position:absolute;left:-4px;right:-4px;top:-17px;height:3px;background:var(--orange)}

/* hero */
.hero{left:0;top:132px;width:1200px;height:540px;background:linear-gradient(180deg,#8a97a2 0%,#b69576 38%,#6a5548 62%,#2d2a2c 80%,#4c4a4c 100%)}
.hero-copy{left:0;top:278px;width:1200px;text-align:center;color:var(--white)}
.hero-copy .kicker{font-family:"Poppins",Arial,sans-serif;font-size:19px;font-weight:500}
.hero-copy h1{color:var(--white);font-size:52px;font-weight:600;margin-top:2px;line-height:1.2}
.hero-copy p{font-size:16px;line-height:1.6;width:640px;margin:12px auto 0;color:#f1f1f1}
.btn{display:inline-flex;align-items:center;gap:10px;font-family:"Poppins",Arial,sans-serif;font-size:14px;font-weight:500;border-radius:3px;text-decoration:none}
.btn-green{background:var(--green);color:var(--white);padding:13px 26px}
.hero-copy .btn{margin-top:26px}
.dots{right:38px;top:378px}
.wave{left:0;top:612px}
.scroll-down{left:576px;top:638px;width:48px;height:48px;border-radius:50%;background:var(--white);display:flex;align-items:center;justify-content:center}

/* about */
.about-photo-ring{left:110px;top:790px;width:366px;height:366px;border-radius:50%;border:10px solid #eef1f4;box-shadow:0 20px 40px rgba(0,0,0,.08)}
.about-photo{left:120px;top:800px;width:346px;height:346px;border-radius:50%;background:linear-gradient(135deg,#d7dfe6 0%,#a9b8c6 45%,#2e63b8 80%,#1c3f86 100%)}
.about-badge{left:338px;top:990px;width:206px;height:206px;border-radius:50%;background:var(--blue);display:flex;align-items:center;justify-content:center;box-shadow:0 12px 30px rgba(26,149,222,.35)}
.about-badge .brand{color:var(--white);font-size:24px}
.about-text{left:568px;top:788px;width:410px}
.about-text h2{font-size:30px;line-height:1.25;font-weight:500}
.underline{width:62px;height:3px;background:var(--green);margin-top:12px}
.about-text p{font-size:13.5px;line-height:1.95;margin-top:30px}
.about-text p + p{margin-top:26px}

/* services */
.section-title{left:0;width:1200px;text-align:center}
.section-title h2{font-size:31px;font-weight:500}
.section-title .underline{margin:14px auto 0}
.cards{left:89px;top:1366px;display:flex;gap:15px}
.card{width:331px;height:258px;border:1px solid var(--line);background:var(--white);padding:30px 33px;position:relative}
.card h3{font-size:21px;margin-top:16px;font-weight:500}
.card p{font-size:13px;line-height:1.75;margin-top:10px}
.card .more{position:absolute;right:33px;bottom:40px;font-family:"Poppins",Arial,sans-serif;font-size:11.5px;color:var(--ink);display:flex;gap:6px;align-items:center;font-weight:500;letter-spacing:.3px}
.card .more.hover{color:var(--green)}

/* cta band */
.cta{left:0;top:1722px;width:1200px;height:390px;background:linear-gradient(120deg,#1b8fd6 0%,#0d85d0 50%,#1a9be0 100%);text-align:center;color:var(--white);padding-top:120px}
.cta h2{color:var(--white);font-size:38px;font-weight:500}
.cta p{font-size:16px;margin-top:8px}
.btn-white{background:var(--white);color:var(--ink);padding:13px 22px;margin-top:26px}

/* why choose */
.why{left:0;top:2112px;width:1200px;height:753px;background:linear-gradient(180deg,#ffffff 0%,#f4f5f7 100%)}
.why-text{left:89px;top:2205px;width:470px}
.why-text h2{font-size:31px;font-weight:500}
.why-text .underline{margin-top:12px}
.why-text .lead{font-size:13.5px;line-height:1.85;margin-top:24px}
.feature{display:flex;gap:18px;margin-top:26px}
.feature h4{font-size:17px;font-weight:500}
.feature p{font-size:13.5px;line-height:1.85;margin-top:6px;width:330px}
.btn-orange{background:var(--orange);color:var(--white);padding:13px 26px;margin-top:36px;box-shadow:0 10px 20px rgba(242,96,47,.3)}
.laptop-screen{left:760px;top:2232px;width:440px;height:500px;background:linear-gradient(90deg,#2b3440 0%,#2b3440 26%,#eef2f6 26%,#f7f9fb 100%);border:10px solid #1c1f24;border-right:none;border-radius:14px 0 0 0}
.laptop-base{left:680px;top:2732px;width:520px;height:22px;background:linear-gradient(180deg,#cfd3d8,#8d939a);border-radius:0 0 0 40px}

/* partners */
.partners{left:0;top:2935px}
.partner-row{left:170px;top:3020px;width:860px;display:flex;justify-content:space-between;align-items:center}
.partner{height:44px;border-radius:6px;background:#dde2e7}

/* newsletter & footer */
.footer{left:0;top:3260px;width:1200px;height:444px;background:var(--dark)}
.newsletter{left:89px;top:3147px;width:1022px;height:195px;background:var(--blue);border-radius:16px;box-shadow:0 16px 30px rgba(0,0,0,.15)}
.newsletter h2{position:absolute;left:52px;top:58px;color:var(--white);font-size:29px;line-height:1.25;font-weight:500}
.subscribe{position:absolute;left:560px;top:72px;width:410px;height:46px;background:var(--white);border-radius:3px;display:flex;align-items:center;justify-content:space-between;padding:0 5px 0 16px;font-size:12.5px;color:var(--muted)}
.subscribe .btn{background:var(--green);color:var(--white);padding:10px 20px;font-size:12.5px}
.footer-brand{left:89px;top:3470px}
.footer-brand .brand{color:var(--white)}
.footer-brand .tagline{color:#aeb7c0}
.fcol{top:3418px;color:#cfd5db;font-size:13px}
.fcol h5{font-family:"Poppins",Arial,sans-serif;font-size:14px;font-weight:500;color:#9aa4ae;margin-bottom:16px}
.fcol li{list-style:none;line-height:2.05;color:var(--white)}
.fcol .c-label{display:flex;gap:8px;align-items:center;color:#c4cbd2;font-size:12.5px}
.fcol .c-val{color:var(--white);margin:2px 0 14px 0}
.social{display:flex;gap:12px}
.social span{width:34px;height:34px;border-radius:50%;display:block}
.footer-rule{left:0;top:3640px;width:1200px;height:1px;background:#36414d}
.copyright{left:0;top:3664px;width:1200px;text-align:center;font-size:12.5px;color:#c8ced4}
.to-top{left:1132px;top:3630px;width:42px;height:42px;border-radius:50%;background:var(--white);display:flex;align-items:center;justify-content:center}
</style>
</head>
<body>

<header class="abs topbar">
  <div class="abs logo"><span class="brand">vale corvan</span><span class="tagline">your IT, networks and security partner</span></div>
  <div class="abs contact-item" style="left:652px;top:20px">
    <svg width="28" height="22" viewBox="0 0 28 22"><rect x="1" y="2" width="26" height="18" rx="2" fill="none" stroke="#1a95de" stroke-width="2"/><path d="M2 4l12 9 12-9" fill="none" stroke="#1a95de" stroke-width="2"/></svg>
    <div><small>Email:</small>info@valecorvanmail.co.uk</div>
  </div>
  <div class="abs contact-item" style="left:880px;top:20px">
    <svg width="24" height="24" viewBox="0 0 24 24"><path d="M5 2l4 1 2 5-3 2c1 3 3 5 6 6l2-3 5 2 1 4-3 3C10 22 2 14 2 5z" fill="none" stroke="#1a95de" stroke-width="1.8" stroke-linejoin="round"/></svg>
    <div><small>Phone:</small>+44 (20) 7946-0321</div>
  </div>
  <div class="abs lang">
    <svg width="14" height="14" viewBox="0 0 14 14"><circle cx="7" cy="7" r="6" fill="none" stroke="#1f2a36" stroke-width="1.2"/><path d="M1 7h12M7 1c-3 3-3 9 0 12M7 1c3 3 3 9 0 12" fill="none" stroke="#1f2a36" stroke-width="1.2"/></svg>EN<svg width="8" height="6" viewBox="0 0 8 6"><path d="M1 1l3 3 3-3" fill="none" stroke="#1f2a36" stroke-width="1.2"/></svg>
  </div>
</header>

<nav class="abs nav">
  <a class="active" href="#">Home</a>
  <a href="#">Services</a>
  <a href="#">About Us</a>
  <a href="#">Contact Us</a>
</nav>

<section class="abs hero" role="img" aria-label="London skyline at dusk with a bridge over the river"></section>
<div class="abs hero-copy">
  <div class="kicker">An IT support and IT Security Company</div>
  <h1>We solve problems</h1>
  <p>Curabitur ullamcorper ultricies nisi nam eget dui etiam rhoncus maecenas tempus, tellus eget condimentum rhoncus.</p>
  <a class="btn btn-green" href="#">Get in touch with us
    <svg width="14" height="10" viewBox="0 0 14 10"><path d="M0 5h12M8 1l4 4-4 4" fill="none" stroke="#fff" stroke-width="1.6"/></svg></a>
</div>
<svg class="abs dots" width="10" height="36" viewBox="0 0 10 36"><circle cx="5" cy="5" r="4" fill="#fff"/><circle cx="5" cy="18" r="3" fill="#ffffff" opacity=".5"/><circle cx="5" cy="31" r="3" fill="#ffffff" opacity=".5"/></svg>
<svg class="abs wave" width="1200" height="62" viewBox="0 0 1200 62" preserveAspectRatio="none"><path d="M0 62 L0 52 C300 50 460 46 520 28 C560 14 640 14 680 28 C740 46 900 50 1200 52 L1200 62 Z" fill="#fff"/></svg>
<div class="abs scroll-down"><svg width="26" height="26" viewBox="0 0 26 26"><circle cx="13" cy="13" r="11" fill="none" stroke="#1f2a36" stroke-width="1.6"/><path d="M8 11l5 5 5-5" fill="none" stroke="#1f2a36" stroke-width="1.8"/></svg></div>

<div class="abs about-photo-ring"></div>
<div class="abs about-photo" role="img" aria-label="Colleagues reviewing documents together in a bright office"></div>
<div class="abs about-badge"><span class="brand">vale corvan</span></div>
<div class="abs about-text">
  <h2>Some short info<br>about our company</h2>
  <div class="underline"></div>
  <p>Aenean vulputate eleifend tellus aenean leo ligula porttitor eu conse quat vitae eleifend ac enim aliquam lorem ante dapibus in viverra quis feugiat a tellus phasellus viverra nulla ut metus varius laoreet quisque rutrum aenean imperdiet etiam ultricies nisi vel augue curabi tur ullam corper ultricies nisi nam eget dui etiam rhoncus maecenas tempus tellus eget condimentum rhoncus, sem quam.</p>
  <p>Maecenas nec odio etstantl ante tincidunt tempus donec vitae sapien ut libero venenatis faucibus nullam quis ante etiam sit amet orci eget eros faucibus tincidunt.</p>
</div>

<div class="abs section-title" style="top:1266px"><h2>Services we provide</h2><div class="underline"></div></div>
<div class="abs cards">
  <article class="card">
    <svg width="48" height="44" viewBox="0 0 48 44"><rect x="24" y="0" width="20" height="14" rx="3" fill="#fde6dc"/><circle cx="18" cy="18" r="8" fill="none" stroke="#f2602f" stroke-width="2"/><path d="M9 18a9 9 0 0118 0M8 18v5M28 18v5" fill="none" stroke="#f2602f" stroke-width="2"/><path d="M4 42c1-9 7-13 14-13s13 4 14 13" fill="none" stroke="#f2602f" stroke-width="2"/></svg>
    <h3>IT Support</h3>
    <p>Aenean vulputate eleifend tellus aenean leo ligula porttitor eu consequat vitae</p>
    <div class="more">LEARN MORE <svg width="12" height="8" viewBox="0 0 12 8"><path d="M0 4h10M7 1l3 3-3 3" fill="none" stroke="currentColor" stroke-width="1.4"/></svg></div>
  </article>
  <article class="card">
    <svg width="48" height="44" viewBox="0 0 48 44"><rect x="0" y="6" width="18" height="14" rx="3" fill="#d9f2df"/><path d="M24 2l16 6v12c0 10-7 17-16 21-9-4-16-11-16-21V8z" fill="none" stroke="#2bb24c" stroke-width="2"/><path d="M16 21l6 6 10-11" fill="none" stroke="#2bb24c" stroke-width="2.4"/></svg>
    <h3>IT Security</h3>
    <p>Aenean vulputate eleifend tellus aenean leo ligula porttitor eu consequat vitae</p>
    <div class="more hover">LEARN MORE <svg width="12" height="8" viewBox="0 0 12 8"><path d="M0 4h10M7 1l3 3-3 3" fill="none" stroke="currentColor" stroke-width="1.4"/></svg></div>
  </article>
  <article class="card">
    <svg width="48" height="44" viewBox="0 0 48 44"><rect x="0" y="14" width="14" height="16" rx="3" fill="#d6ecfa"/><rect x="10" y="2" width="12" height="10" rx="2" fill="none" stroke="#1a95de" stroke-width="2"/><rect x="26" y="2" width="12" height="10" rx="2" fill="none" stroke="#1a95de" stroke-width="2"/><circle cx="16" cy="22" r="4" fill="none" stroke="#1a95de" stroke-width="2"/><circle cx="32" cy="22" r="4" fill="none" stroke="#1a95de" stroke-width="2"/><path d="M8 42c0-8 4-12 8-12s8 4 8 12M24 42c0-8 4-12 8-12s8 4 8 12" fill="none" stroke="#1a95de" stroke-width="2"/></svg>
    <h3>IT Consulting</h3>
    <p>Aenean vulputate eleifend tellus aenean leo ligula porttitor eu consequat vitae</p>
    <div class="more">LEARN MORE <svg width="12" height="8" viewBox="0 0 12 8"><path d="M0 4h10M7 1l3 3-3 3" fill="none" stroke="currentColor" stroke-width="1.4"/></svg></div>
  </article>
</div>

<section class="abs cta">
  <h2>Get in touch with us</h2>
  <p>Aenean vulputate eleifend tellus aenean leo ligula porttitor eu.</p>
  <a class="btn btn-white" href="#">Contact us <svg width="12" height="8" viewBox="0 0 12 8"><path d="M0 4h10M7 1l3 3-3 3" fill="none" stroke="#1f2a36" stroke-width="1.4"/></svg></a>
</section>

<section class="abs why"></section>
<div class="abs why-text">
  <h2>Why choose us</h2>
  <div class="underline"></div>
  <p class="lead">Quisque rutrum aenean imperdiet etiam ultricies nisi vel augue cura bitur ullamcorper ultricies nisi nam eget dui etiam.</p>
  <div class="feature" style="margin-top:30px">
    <svg width="30" height="26" viewBox="0 0 30 26"><path d="M2 24h26" stroke="#1a95de" stroke-width="2"/><rect x="5" y="12" width="4" height="10" fill="none" stroke="#1a95de" stroke-width="2"/><rect x="13" y="6" width="4" height="16" fill="none" stroke="#1a95de" stroke-width="2"/><rect x="21" y="2" width="4" height="20" fill="none" stroke="#1a95de" stroke-width="2"/></svg>
    <div><h4>We Are Brightforce</h4><p>Sit amet adipiscing sem neque sed ipsum nam quam nunc blandit vel luctus pulvinar hendrerit id.</p></div>
  </div>
  <div class="feature">
    <svg width="30" height="26" viewBox="0 0 30 26"><circle cx="15" cy="8" r="6" fill="none" stroke="#f2602f" stroke-width="2"/><path d="M4 25c1-7 5-10 11-10s10 3 11 10" fill="none" stroke="#f2602f" stroke-width="2"/></svg>
    <div><h4>Customers Are #1</h4><p>Sit amet adipiscing sem neque sed ipsum nam quam nunc blandit vel luctus pulvinar hendrerit id.</p></div>
  </div>
  <div class="feature">
    <svg width="30" height="26" viewBox="0 0 30 26"><path d="M15 24L4 13a6 6 0 0111-8 6 6 0 0111 8z" fill="none" stroke="#2bb24c" stroke-width="2"/></svg>
    <div><h4>No Hassles Here</h4><p>Sit amet adipiscing sem neque sed ipsum nam quam nunc blandit vel luctus pulvinar hendrerit id.</p></div>
  </div>
  <a class="btn btn-orange" href="#">Contact us <svg width="12" height="8" viewBox="0 0 12 8"><path d="M0 4h10M7 1l3 3-3 3" fill="none" stroke="#fff" stroke-width="1.4"/></svg></a>
</div>
<div class="abs laptop-screen" role="img" aria-label="Laptop showing a business management dashboard with module tiles"></div>
<div class="abs laptop-base"></div>

<div class="abs section-title partners"><h2>Our Partners</h2><div class="underline"></div></div>
<div class="abs partner-row">
  <div class="partner" style="width:138px"></div>
  <div class="partner" style="width:136px"></div>
  <div class="partner" style="width:134px"></div>
  <div class="partner" style="width:130px"></div>
  <div class="partner" style="width:98px"></div>
</div>

<footer class="abs footer"></footer>
<div class="abs newsletter">
  <h2>Subscribe to<br>our email newsletter</h2>
  <div class="subscribe">Enter your email newsletter
    <span class="btn">Subscribe <svg width="12" height="8" viewBox="0 0 12 8"><path d="M0 4h10M7 1l3 3-3 3" fill="none" stroke="#fff" stroke-width="1.4"/></svg></span>
  </div>
</div>
<div class="abs footer-brand logo"><span class="brand">vale corvan</span><span class="tagline">your IT, networks and security partner</span></div>
<div class="abs fcol" style="left:338px">
  <h5>Quick links</h5>
  <ul><li>› Home</li><li>› Services</li><li>› About us</li><li>› Contact us</li></ul>
</div>
<div class="abs fcol" style="left:563px">
  <h5>Contact</h5>
  <div class="c-label"><svg width="12" height="12" viewBox="0 0 24 24"><path d="M5 2l4 1 2 5-3 2c1 3 3 5 6 6l2-3 5 2 1 4-3 3C10 22 2 14 2 5z" fill="#f2602f"/></svg>Phone:</div>
  <div class="c-val">(020) 7946-0457</div>
  <div class="c-label"><svg width="13" height="10" viewBox="0 0 13 10"><rect x=".5" y=".5" width="12" height="9" rx="1" fill="none" stroke="#f2602f"/><path d="M1 1l5.5 4L12 1" fill="none" stroke="#f2602f"/></svg>Email:</div>
  <div class="c-val">info@valecorvanmail.co.uk</div>
</div>
<div class="abs fcol" style="left:845px">
  <h5>Let's get social</h5>
  <div class="social"><span style="background:#3b5a9a"></span><span style="background:#2a70a8"></span><span style="background:#d93a2b"></span><span style="background:#c1357f"></span></div>
</div>
<div class="abs footer-rule"></div>
<div class="abs copyright">© 2018, All Rights Reserved.</div>
<div class="abs to-top"><svg width="14" height="14" viewBox="0 0 14 14"><path d="M7 13V2M2 7l5-5 5 5" fill="none" stroke="#1f2a36" stroke-width="1.8"/></svg></div>

</body>
</html>
```